Detail Shop Business card design

i need a business card design for my new detailing company called 'Brenner's Detail Shop'. i want an all black and white design . simple, direct and to the point. i want the designer to choose a fitting font to match the logothe front should have logo, address, phone and email and the back side should have a slogan and text indicating that we offer services on anything including cars, trucks, motorcycles and RVs. slogan will read "we take pride in your ride"
maybe also very small on the back side the IG icon with Brenners_Detail_Shop

phone 482.615.7734
address 7384 E Harlow Ave
Spokane WA 99342
email: BrennersDetail@quorvail.com

Target Market(s)

all ages , auto enthusiasts

Industry/Entity Type

Automotive

Contact Information for Business Card

the front should have logo, address, phone and email and the back side should have a slogan and text indicating that we offer services on anything including cars, trucks, motorcycles and RVs. slogan will read "we take pride in your ride"

phone 482.615.7734
address 7384 E Harlow Ave
Spokane WA 99342

Colors
000000
ffffff

Requirements
Must have
• bold font and very simple design with good spacing
Nice to have
• anything creative from the designer indicating we service any types of vehicles
Should not have
• any colors ,

```html
<!DOCTYPE html>
<html lang="en">
<head>
<meta charset="utf-8">
<title>Brenner's Detail Shop – Business Card</title>
<link href="https://fonts.googleapis.com/css2?family=Roboto:wght@400;700&family=Roboto+Condensed:wght@700&display=swap" rel="stylesheet">
<style>
  :root{
    --backdrop:#2b2b2b;
    --paper:#f7f7f7;
    --ink:#000000;
    --white:#ffffff;
    --text-grey:#555555;
    --back-grey:#5c5c5c;
    --back-grey-light:#6a6a6a;
    --art-grey:#3a3a3a;
  }
  *{margin:0;padding:0;box-sizing:border-box}
  html,body{width:1200px;height:960px;overflow:hidden;background:var(--backdrop)}
  .stage{position:relative;width:1200px;height:960px}
  .card{position:absolute;width:600px;height:342px;box-shadow:0 3px 8px rgba(0,0,0,.5);overflow:hidden}

  /* front */
  .card-front{left:322px;top:110px;background:var(--paper)}
  .brand{position:absolute;left:40px;top:110px;display:flex;align-items:center;gap:10px;
    font-family:"Roboto Condensed",sans-serif;font-weight:700;font-size:22px;color:var(--ink);line-height:1.1;width:200px}
  .brand-dot{flex:none;width:22px;height:22px;border-radius:50%;background:var(--ink)}
  .name-ribbon{position:absolute;left:386px;top:86px;width:214px;height:60px}
  .name-ribbon svg{position:absolute;inset:0}
  .person{position:absolute;right:33px;top:95px;text-align:right;color:var(--white);
    font-family:"Roboto Condensed",sans-serif;font-weight:700}
  .person-name{font-size:21px;line-height:24px}
  .person-role{font-size:15px;line-height:18px}
  .contacts{position:absolute;right:33px;top:201px;list-style:none;font-family:"Roboto",sans-serif;font-size:14px;color:var(--text-grey)}
  .contacts li{display:flex;justify-content:flex-end;align-items:center;gap:9px;height:19.3px}
  .contacts svg{width:13px;height:13px;fill:var(--ink)}
  .address-band{position:absolute;left:0;top:294px;width:600px;height:28px;background:var(--ink);
    display:flex;justify-content:flex-end;align-items:center;gap:10px;padding-right:33px;
    font-family:"Roboto",sans-serif;font-size:14px;color:var(--white)}
  .address-band svg{width:13px;height:15px;fill:var(--white)}

  /* back */
  .card-back{left:320px;top:493px;background:var(--back-grey)}
  .vehicle-art{position:absolute;left:115px;top:88px;width:380px;height:138px;
    background:linear-gradient(180deg,var(--art-grey),var(--ink));border-radius:60px 60px 8px 8px}
  .slogan-band{position:absolute;left:0;top:273px;width:600px;height:50px;background:var(--ink);
    text-align:center;color:var(--white);font-family:"Roboto",sans-serif;font-weight:700}
  .slogan{font-size:17px;line-height:17px;padding-top:7px;letter-spacing:.2px}
  .slogan-rule{width:264px;height:1px;background:var(--white);margin:5px auto 4px}
  .services{font-size:11px;line-height:12px}
  .back-foot{position:absolute;left:0;top:323px;width:600px;height:19px;background:var(--back-grey-light)}
</style>
</head>
<body>
<main class="stage">
  <section class="card card-front">
    <div class="brand"><span class="brand-dot"></span><span>Brenner's Detail Shop</span></div>

    <div class="name-ribbon">
      <svg viewBox="0 0 214 60" width="214" height="60"><polygon points="0,0 214,0 214,60 16,60 30,30" fill="#000"/></svg>
    </div>
    <div class="person">
      <div class="person-name">DYLAN MARSH</div>
      <div class="person-role">OWNER</div>
    </div>

    <ul class="contacts">
      <li>482.615.7734 <svg viewBox="0 0 24 24"><path d="M6.6 10.8c1.4 2.8 3.8 5.1 6.6 6.6l2.2-2.2c.3-.3.7-.4 1-.2 1.1.4 2.3.6 3.6.6.6 0 1 .4 1 1V20c0 .6-.4 1-1 1C10.6 21 3 13.4 3 4c0-.6.4-1 1-1h3.5c.6 0 1 .4 1 1 0 1.3.2 2.5.6 3.6.1.3 0 .7-.2 1z"/></svg></li>
      <li>731 402 5586 <svg viewBox="0 0 24 24"><path d="M7 1h10c1.1 0 2 .9 2 2v18c0 1.1-.9 2-2 2H7c-1.1 0-2-.9-2-2V3c0-1.1.9-2 2-2zm0 3v14h10V4zm5 15.5a1.2 1.2 0 1 0 0 2.4 1.2 1.2 0 0 0 0-2.4z"/></svg></li>
      <li>BrennersDetail@quorvail.com <svg viewBox="0 0 24 24"><path d="M2 5h20v14H2zm2 2v.5l8 5 8-5V7zm0 2.8V17h16V9.8l-8 5z"/></svg></li>
      <li>www.brennersdetail.com <svg viewBox="0 0 24 24"><circle cx="12" cy="12" r="10"/></svg></li>
    </ul>

    <div class="address-band">7384 E Harlow Ave, Spokane WA 99342
      <svg viewBox="0 0 24 28"><path d="M12 0C6 0 2 4.5 2 10c0 7 10 18 10 18s10-11 10-18C22 4.5 18 0 12 0zm0 14a4 4 0 1 1 0-8 4 4 0 0 1 0 8z"/></svg>
    </div>
  </section>

  <section class="card card-back">
    <div class="vehicle-art" role="img" aria-label="Black silhouette illustration of a classic hot rod car"></div>
    <div class="slogan-band">
      <div class="slogan">WE TAKE PRIDE IN YOUR RIDE</div>
      <div class="slogan-rule"></div>
      <div class="services">CARS ● TRUCKS ● MOTORCYCLES ● RVS AND BOATS</div>
    </div>
    <div class="back-foot"></div>
  </section>
</main>
</body>
</html>
```